Chocoloate confectionery company requires vibrant Packaging Design for a mini chocolate bar

- Need a packaging design for a new product; a chocolate mini-bar.
- Our corporate colors of brown and pink should be included in design.
- The chocolate weighs 20grams and measures 8 cm length x 5 cm width x 1 cm depth
- It will be covered in gold foil and wrapped in a paper sleeve.
- The paper sleeve measures 13.5 cm length x 7.5 cm width
- The paper sleeve can then be sectioned into 3 equal areas
- The packaging design is required on middle section of the sleeve.
- The ingredients, company details, barcode and disclaimer etc will be on the right section
- The left section of the sleeve may be left blank

PLEASE SEE SAMPLE PICTURES PER ATTACHED

Target Market(s)

Everyday shoppers (e.g. Moms, Dads, kids, teens, students)

Industry/Entity Type

It Company

Requirements
Must have
• Brown and pink colors (as per business card attached)
Name of mini chocolate bar is Mallow Nib. This must appear on middle section of paper sleeve

```html
<!DOCTYPE html>
<html lang="en">
<head>
<meta charset="utf-8">
<title>Mallow Nib Sweet Shop – Mini Bar Wrapper</title>
<link rel="stylesheet" href="https://fonts.googleapis.com/css2?family=Lobster&family=Courgette&display=swap">
<style>
  :root {
    --canvas-bg: #ffffff;
    --wrapper-yellow: #fbbd0a;
    --crimp-yellow: #e9c417;
    --crimp-line: #b99a10;
    --fold-shade: #e0a206;
    --splash-dark: #2a1a10;
    --splash-edge: #ffffff;
    --bar-brown: #8e3f1a;
    --bar-dark: #5e2a10;
    --brand-orange: #c9581f;
    --brand-light: #f08a3c;
    --flavour-pink: #e8325a;
    --text-white: #ffffff;
  }
  html, body {
    margin: 0;
    padding: 0;
    width: 1200px;
    height: 598px;
    overflow: hidden;
    background: var(--canvas-bg);
  }
  .wrapper-art {
    display: block;
    width: 1200px;
    height: 598px;
  }
  .wrapper-body { fill: var(--wrapper-yellow); }
  .crimp { fill: url(#crimp-lines); }
  .fold { fill: var(--fold-shade); opacity: 0.7; }
  .splash { fill: var(--splash-dark); stroke: var(--splash-edge); stroke-width: 10; stroke-linejoin: round; }
  .bar-character rect { fill: var(--bar-brown); stroke: var(--bar-dark); stroke-width: 2; }
  .brand-name {
    font-family: "Lobster", cursive;
    font-size: 90px;
    fill: var(--brand-orange);
  }
  .shop-tagline {
    font-family: "Courgette", cursive;
    font-size: 46px;
    fill: var(--text-white);
  }
  .flavour-band { fill: var(--flavour-pink); }
  .flavour-label {
    font-family: "Courgette", cursive;
    font-size: 28px;
    fill: var(--text-white);
  }
</style>
</head>
<body>
<svg class="wrapper-art" viewBox="0 0 1200 598" xmlns="http://www.w3.org/2000/svg">
  <defs>
    <pattern id="crimp-lines" width="8" height="10" patternUnits="userSpaceOnUse">
      <rect width="8" height="10" fill="#e9c417"/>
      <rect x="0" y="4" width="8" height="3" fill="#b99a10"/>
    </pattern>
    <clipPath id="wrapper-clip">
      <path d="M48,42 L150,42 Q600,62 1065,42 L1142,42 L1142,547 L1065,547 Q600,528 150,547 L48,547 Z"/>
    </clipPath>
  </defs>

  <g clip-path="url(#wrapper-clip)">
    <rect class="wrapper-body" x="0" y="0" width="1200" height="598"/>
    <rect class="crimp" x="48" y="40" width="102" height="510"/>
    <rect class="crimp" x="1065" y="40" width="80" height="510"/>
    <rect class="fold" x="150" y="40" width="22" height="510"/>
    <rect class="fold" x="1040" y="40" width="25" height="510"/>

    <g class="bar-character" role="img" aria-label="Mustached chocolate bar character holding a strawberry">
      <rect x="110" y="50" width="175" height="250" rx="6" transform="rotate(-8 197 175)"/>
    </g>
    <g class="bar-character" role="img" aria-label="Small chocolate bar character">
      <rect x="50" y="320" width="75" height="100" rx="4" transform="rotate(-25 87 370)"/>
    </g>
    <g class="bar-character" role="img" aria-label="Small chocolate bar character">
      <rect x="185" y="490" width="60" height="70" rx="4" transform="rotate(-15 215 525)"/>
    </g>
    <g class="bar-character" role="img" aria-label="Small chocolate bar character">
      <rect x="390" y="455" width="90" height="80" rx="4" transform="rotate(-25 435 495)"/>
    </g>
    <g class="bar-character" role="img" aria-label="Small chocolate bar character with strawberry">
      <rect x="640" y="65" width="65" height="55" rx="4" transform="rotate(-10 672 92)"/>
    </g>
    <g class="bar-character" role="img" aria-label="Chocolate bar character with strawberry">
      <rect x="860" y="175" width="85" height="95" rx="4" transform="rotate(-30 902 222)"/>
    </g>
    <g class="bar-character" role="img" aria-label="Small chocolate bar character">
      <rect x="1080" y="265" width="55" height="75" rx="4" transform="rotate(-25 1107 302)"/>
    </g>
    <g class="bar-character" role="img" aria-label="Small chocolate bar character with strawberry">
      <rect x="1035" y="45" width="60" height="65" rx="4" transform="rotate(-10 1065 77)"/>
    </g>
    <g class="bar-character" role="img" aria-label="Upside-down chocolate bar character with strawberry">
      <rect x="845" y="355" width="105" height="185" rx="5" transform="rotate(-4 897 447)"/>
    </g>

    <path class="flavour-band" d="M935,547 L1142,352 L1142,418 L1005,547 Z"/>
    <text class="flavour-label" x="1062" y="462" text-anchor="middle" transform="rotate(-43 1062 462)">Struberry</text>
  </g>

  <path class="splash" d="M335,215 C330,175 380,160 430,168 C470,174 500,150 530,128 C570,104 610,118 650,130 C700,146 740,130 780,150 C820,172 835,215 850,255 C865,300 850,330 820,335 C790,340 790,380 770,420 C750,465 700,468 665,445 C635,425 600,440 560,455 C520,470 470,460 440,435 C410,410 395,400 355,395 C315,388 300,350 310,320 C320,290 340,265 335,215 Z"/>
  <g class="bar-character" role="img" aria-label="Chocolate bar character with strawberry on the splash">
    <rect x="537" y="118" width="66" height="108" rx="4"/>
  </g>

  <text class="brand-name" x="560" y="322" text-anchor="middle">Mallow Nib</text>
  <text class="shop-tagline" x="560" y="380" text-anchor="middle">Sweet Shop</text>
</svg>
</body>
</html>
```